The Velvet Needle Poster for a shop Facade

Hello Designers,

• We have a 4X4 meters façade for our tailor shop “The Velvet Needle”, and we are looking for a unique, simple and attractive poster to be printed on the glass to attract the attention of the driving customers or whoever passes by the shop.
• The Velvet Needle, with ‘Velvet’ referring to door-to-door service, our concept as follows (Call … Measure … Stitch … Deliver)

1. Step1: Book online or simply call us to make your appointment (should be pictorial not writing)
2. Step2: Our dedicated personnel will come to you at your preferred time and location. (should be pictorial not writing)
3. Step3: Clothes Alteration/Making to suit your style and body fit. (should be pictorial not writing)
4. Step4: Delivery on completion, at your preferred time and location. (should be pictorial not writing)

• We are specialized in clothes alteration and making for both men and women, and anything related to tailoring services www.thevelvetneedle-example.com

• The poster must include the name “The Velvet Needle” as well as the phone number 04 312 8817 in a very clear and obvious way (logo will be optional if you can show it in a nice way)
And the concept of our shop should be shown in the poster in a very simple and clear way and more graphical than words. (Perhaps a graphical flow to show client booking our service and we go to their place for alterations done).
Colors should be chosen carefully to attract the customers and the walk-ins eyes when they pass by either walking or by cars.

Thank you
Rami

Target Market(s)

We have a 4X4 meters façade for our tailor shop “The Velvet Needle”, and we are looking for a unique, simple and attractive poster to be printed on the glass to attract the attention of the driving customers or whoever passes by the shop.

Industry/Entity Type

Fashion

• to match the poster/signage

Colors

Designer to choose colors to be used in the design.

Requirements
Must have
Nice to have
• the concept of our shop should be shown in the poster in a very simple and clear way and more graphical than words. (Perhaps a graphical flow to show client booking our service and we go to their place for alterations done).
Should not have
• many words, copied designs. Please only use the images attached in the project brief for reference.

```html
<!DOCTYPE html>
<html lang="en">
<head>
<meta charset="utf-8">
<title>The Velvet Needle – Facade Poster</title>
<link rel="stylesheet" href="https://fonts.googleapis.com/css2?family=Limelight&family=Open+Sans:wght@600&family=Questrial&display=swap">
<style>
  :root {
    --ink-dark: #0b0508;
    --plum-deep: #2a1420;
    --plum-mid: #3a1c2c;
    --ribbon-edge: #3c0f30;
    --ribbon-mid: #5c2e52;
    --ribbon-light: #9a8a98;
    --white: #ffffff;
  }
  html, body {
    margin: 0;
    padding: 0;
    width: 1200px;
    height: 1200px;
    overflow: hidden;
    background: var(--ink-dark);
  }
  .poster {
    position: relative;
    width: 1200px;
    height: 1200px;
    overflow: hidden;
  }
  .photo-backdrop {
    position: absolute;
    inset: 0;
    background:
      radial-gradient(ellipse 55% 45% at 50% 55%, var(--plum-mid) 0%, var(--plum-deep) 45%, var(--ink-dark) 100%);
  }
  .brand-mark {
    position: absolute;
    left: 410px;
    top: 152px;
    width: 380px;
    height: 380px;
    border: 2px solid var(--white);
    border-radius: 50%;
    box-sizing: border-box;
  }
  .brand-name {
    position: absolute;
    left: 0;
    width: 1200px;
    top: 270px;
    margin: 0;
    text-align: center;
    font-family: "Questrial", sans-serif;
    font-weight: 400;
    font-size: 54px;
    line-height: 64px;
    letter-spacing: 2px;
    color: var(--white);
  }
  .tagline {
    position: absolute;
    left: 0;
    width: 1200px;
    top: 562px;
    margin: 0;
    text-align: center;
    font-family: "Questrial", sans-serif;
    font-size: 19px;
    line-height: 28px;
    letter-spacing: 9px;
    color: var(--white);
  }
  .ribbon {
    position: absolute;
    left: 122px;
    top: 756px;
    width: 956px;
    height: 150px;
  }
  .ribbon-title {
    position: absolute;
    left: 0;
    width: 1200px;
    top: 780px;
    margin: 0;
    text-align: center;
    font-family: "Limelight", serif;
    font-weight: 400;
    font-size: 78px;
    line-height: 100px;
    color: var(--white);
  }
  .call-line {
    position: absolute;
    left: 0;
    width: 1200px;
    top: 960px;
    margin: 0;
    text-align: center;
    font-family: "Open Sans", sans-serif;
    font-weight: 600;
    color: var(--white);
    white-space: nowrap;
  }
  .call-label { font-size: 70px; letter-spacing: -1px; }
  .call-number { font-size: 88px; word-spacing: 10px; margin-left: 18px; }
</style>
</head>
<body>
  <main class="poster">
    <div class="photo-backdrop" role="img" aria-label="Dark photograph of a tailor's hands measuring a client's wrist with a tape measure"></div>

    <div class="brand-mark"></div>
    <h2 class="brand-name">The Velvet<br>Needle</h2>
    <p class="tagline">Clothes<br>Alterations</p>

    <svg class="ribbon" viewBox="0 0 956 150" aria-hidden="true">
      <defs>
        <linearGradient id="ribbonFill" x1="0" y1="0" x2="1" y2="0">
          <stop offset="0" stop-color="var(--ribbon-edge)"/>
          <stop offset="0.25" stop-color="var(--ribbon-mid)"/>
          <stop offset="0.5" stop-color="var(--ribbon-light)"/>
          <stop offset="0.75" stop-color="var(--ribbon-mid)"/>
          <stop offset="1" stop-color="var(--ribbon-edge)"/>
        </linearGradient>
      </defs>
      <polygon points="0,0 956,0 912,75 956,150 0,150 44,75" fill="url(#ribbonFill)"/>
    </svg>
    <h1 class="ribbon-title">The Velvet Needle</h1>

    <p class="call-line"><span class="call-label">Call Us:</span><span class="call-number">04 312 8817</span></p>
  </main>
</body>
</html>
```